Advanced Therapeutic Massage Therapist

I need a business card advertising my massage services as an advanced therapeutic massage therapist. I offer advanced therapeutic massage, swedish and deep tissue. I want to create a simple, professional and feminine card. I like bright colours and creativity.

I prefer a bold and experimental approach rather than something status-quo. A card to suggest therapeutic healing through dynamic massage. Motifs, shapes or layout which suggest movement and flow.
Updates

Target Market(s)

Everybody!

Industry/Entity Type

Health And Wellness

Contact Information for Business Card

The card should include:
My name, logo, services offered and my contact details.

Aoibhín Delaney
Massage Therapist

- Swedish - Deep Tissue - Advanced Therapeutic

Phone: (+353) 87 261 9043
Email: regenerate@aoibhindelaney-example.com
Website: www.aoibhindelany-example.com

Font styles to use
Serif
Sans Serif
Decorative
Script

Colors

Designer to choose colors to be used in the design.

Requirements
Must have
• An example may contain something like this, yet concise:
• "Aoibhín Delaney
• Massage Therapist
• - Swedish - Deep Tissue - Advanced Therapeutic"
Nice to have
• This sentence is optional:
• Imagery such as a logo or symbol. I have attached a file containing a logo I had produced however the name is incorrect now as it is "Aoibhín" not "Evie". It could be edited to change it to Aoibhín.
• I have sent the file as .psd .jpg. .pdf and .png
• I like when the card conveys energy, movement, pressure points, flow etc.
• I just like the designer to follow their own style and ideas. I like bright colours but must have a lot of a base colour to offset it. I really prefer them to follow their own inspiration. That is my preference.
Should not have
• Pine trees, non-native trees to Britain and Ireland, exotic flowers or animals that are not native to Britain and Ireland.
• I don't like brown as the background colour of the card.
• The cars shouldn't look like a wedding invitation i.e too many floral type designs.

```html
<!DOCTYPE html>
<html lang="en">
<head>
<meta charset="utf-8">
<title>Aoibhín Delaney – Massage Therapist Card</title>
<link href="https://fonts.googleapis.com/css2?family=Pinyon+Script&family=Lora:ital,wght@0,400;0,600;1,600&display=swap" rel="stylesheet">
<style>
  :root {
    --backdrop: #2b2b2d;
    --mint: #a9e3d6;
    --mint-deep: #8fd3c4;
    --gold: #b8803a;
    --paper: #fffdfb;
    --ink: #2c2c2c;
    --accent: #6cc7b3;
  }
  * { margin: 0; padding: 0; box-sizing: border-box; }
  html, body { width: 1200px; height: 1200px; overflow: hidden; }
  body {
    background: var(--backdrop);
    display: flex; flex-direction: column; align-items: center; justify-content: center;
    gap: 40px;
    font-family: "Lora", Georgia, serif;
    color: var(--ink);
  }
  .card-panel {
    position: relative;
    width: 900px; height: 530px;
    border-radius: 34px;
    overflow: hidden;
  }
  .border-pattern {
    position: absolute; inset: 0;
    background: linear-gradient(135deg, var(--mint) 0%, #c9e6d8 45%, #d9bf8e 75%, var(--mint-deep) 100%);
  }
  .inner-panel {
    position: absolute; inset: 62px 70px;
    background: var(--paper);
    display: flex; flex-direction: column; align-items: center; justify-content: center;
    text-align: center;
  }
  .name {
    font-family: "Pinyon Script", cursive;
    font-size: 58px; line-height: 1.1; color: var(--ink);
  }
  .role { font-size: 22px; margin-top: 4px; letter-spacing: 0.5px; }
  .divider { margin: 14px 0; }
  .contact-line {
    display: flex; align-items: center; gap: 10px;
    font-size: 20px;
  }
  .contact-line svg { flex: none; }
  .web-line { margin-top: 14px; font-size: 18px; }
  .services {
    margin-top: 18px; font-size: 19px;
    display: flex; align-items: center; gap: 14px;
  }
  .star { color: var(--accent); font-size: 16px; }
  .brand {
    display: flex; flex-direction: column; align-items: center; gap: 10px;
  }
  .brand-mark {
    width: 110px; height: 110px; border-radius: 50%;
    background: radial-gradient(circle, var(--mint) 0%, var(--accent) 100%);
  }
  .brand-name {
    font-family: "Pinyon Script", cursive;
    font-size: 40px; color: #6f6f6f;
  }
  .brand-sub { font-size: 13px; letter-spacing: 3px; color: #9a9a9a; text-transform: uppercase; margin-top: -8px; }
  .tagline {
    margin-top: 22px;
    font-style: italic; font-weight: 600; font-size: 21px; line-height: 1.35;
  }
</style>
</head>
<body>

  <section class="card-panel card-inside">
    <div class="border-pattern" role="img" aria-label="Mint background with flowing gold swirl ornament"></div>
    <div class="inner-panel">
      <div class="name">Aoibhín Delaney</div>
      <div class="role">Massage Therapist</div>
      <svg class="divider" width="60" height="14" viewBox="0 0 60 14" aria-hidden="true">
        <path d="M2 7 Q15 0 30 7 T58 7" fill="none" stroke="var(--accent)" stroke-width="2"/>
      </svg>
      <div class="contact-line">
        <svg width="20" height="20" viewBox="0 0 24 24" aria-hidden="true"><path fill="var(--accent)" d="M6.6 10.8a15 15 0 0 0 6.6 6.6l2.2-2.2a1 1 0 0 1 1-.25 11.4 11.4 0 0 0 3.6.57 1 1 0 0 1 1 1V20a1 1 0 0 1-1 1A17 17 0 0 1 3 4a1 1 0 0 1 1-1h3.5a1 1 0 0 1 1 1c0 1.25.2 2.45.57 3.6a1 1 0 0 1-.25 1z"/></svg>
        <span>(+353) 87 261 9043</span>
      </div>
      <svg class="divider" width="60" height="14" viewBox="0 0 60 14" aria-hidden="true">
        <path d="M2 7 Q15 0 30 7 T58 7" fill="none" stroke="var(--accent)" stroke-width="2"/>
      </svg>
      <div class="contact-line web-line">
        <svg width="18" height="18" viewBox="0 0 24 24" aria-hidden="true"><circle cx="12" cy="12" r="10" fill="var(--accent)"/></svg>
        <span>www.aoibhinmassage-example.com | aoibhinmassage@example-mail.com</span>
      </div>
      <div class="services">
        <span>Swedish</span><span class="star">★</span><span>Deep Tissue</span><span class="star">★</span><span>Advanced Therapeutic</span>
      </div>
    </div>
  </section>

  <section class="card-panel card-front">
    <div class="border-pattern" role="img" aria-label="Mint background with flowing gold swirl ornament"></div>
    <div class="inner-panel">
      <div class="brand">
        <div class="brand-mark"></div>
        <div class="brand-name">Aoibhín Delaney</div>
        <div class="brand-sub">massage therapy</div>
      </div>
      <p class="tagline">QTEC qualified specialising in<br>advanced therapeutic and deep tissue massage</p>
    </div>
  </section>

</body>
</html>
```